Sport Celebration Day Poster

The poster should highlight the sport of archery and bring awareness to the sport and invite people to come and try archery. We have a logo that must be featured, as well as a sample photos that can be used in the creative process, but do not necessarily have to be featured. The feel of the poster should be fun and inviting and have archery imagery (bows, arrows, targets, etc.).

The poster must feature the date MAY 11, 2019 and "Try Archery."

We would like to see an area where our sport clubs can fill in their own information including sections for "Name, Date, Location, Times, Location, Email, Website, and Notes."

Submissions should include some of these colours or colours from the logo:
Blue #00A1EF, Grey #313A43, Green #406C1D, Red #DC2F31, Yellow #FDDD39

```html
<!DOCTYPE html>
<html lang="en">
<head>
<meta charset="utf-8">
<title>Try Archery – Bullseye Day</title>
<link rel="stylesheet" href="https://fonts.googleapis.com/css2?family=Permanent+Marker&family=Montserrat:wght@700&family=Archivo+Narrow:wght@700&display=swap">
<style>
  :root{
    --red:#dc2f31;
    --red-deep:#b81d24;
    --grey:#313a43;
    --grey-mid:#5d6168;
    --olive:#6b6a55;
    --blue:#00a1ef;
    --yellow:#fddd39;
    --white:#ffffff;
    --ink:#1e1e1e;
  }
  *{margin:0;padding:0;box-sizing:border-box}
  html,body{width:900px;height:1200px;overflow:hidden;background:var(--white)}
  .poster{position:relative;width:900px;height:1200px;overflow:hidden;background:var(--grey)}
  .hero-photo{
    position:absolute;inset:0;
    background:
      radial-gradient(ellipse 260px 520px at 450px 520px, rgba(20,20,20,.55), rgba(20,20,20,0) 70%),
      linear-gradient(90deg, var(--red-deep) 0%, var(--red) 30%, #8e1a1f 50%, var(--olive) 50%, var(--grey-mid) 75%, #8a8c90 100%);
  }
  .club-mark{
    position:absolute;left:632px;top:112px;width:200px;
    font-family:'Montserrat',sans-serif;font-weight:700;font-size:24px;line-height:1.05;
    color:var(--red);text-align:center;letter-spacing:.5px;
  }
  .event-mark{
    position:absolute;left:386px;top:170px;width:170px;
    display:flex;align-items:center;gap:8px;
    font-family:'Montserrat',sans-serif;font-weight:700;font-size:24px;line-height:1;color:var(--yellow);
  }
  .event-mark .dot{width:30px;height:30px;border-radius:50%;background:var(--yellow);flex:none}
  .headline{
    position:absolute;left:0;width:900px;text-align:center;
    font-family:'Permanent Marker',sans-serif;font-weight:400;color:var(--white);line-height:1;
  }
  .headline-try{top:280px;font-size:150px;padding-left:10px}
  .headline-archery{top:430px;font-size:150px;padding-left:30px;letter-spacing:-2px}
  .event-date{
    position:absolute;left:0;width:900px;top:624px;text-align:center;padding-left:20px;
    font-family:'Montserrat',sans-serif;font-weight:700;font-size:34px;letter-spacing:2px;color:var(--white);
  }
  .info-disc{position:absolute;left:0;top:0;width:900px;height:1200px}
  .club-form{
    position:absolute;left:74px;top:786px;width:332px;
    font-family:'Archivo Narrow',sans-serif;font-weight:700;font-size:19px;color:var(--ink);
  }
  .form-row{display:flex;align-items:flex-end;height:31.5px}
  .form-row .label{flex:none;padding-right:8px}
  .form-row .line{flex:1;border-bottom:1.5px solid var(--ink);margin-bottom:5px}
  .partners{position:absolute;left:76px;top:1084px;display:flex;align-items:center;gap:22px}
  .partner{background:#e7e7e7;border:2px solid var(--red)}
  .partner.round{width:30px;height:30px;border-radius:50%}
  .partner.wide{width:100px;height:26px;border:none;background:#d9d9d9}
  .partner.mid{width:64px;height:36px;border:none;background:#e3d3ae}
  .partner.small{width:52px;height:28px;border:none;background:#e6e6e6}
</style>
</head>
<body>
<main class="poster">
  <div class="hero-photo" role="img" aria-label="Young archer in a split red and grey training shirt holding a recurve bow, arrows in a quiver at the left"></div>

  <div class="club-mark">NORTHBOW<br>ARCHERY</div>
  <div class="event-mark"><span class="dot"></span><span>BULLSEYE<br>DAY</span></div>

  <h1 class="headline headline-try">TRY</h1>
  <h1 class="headline headline-archery">ARCHERY!</h1>
  <p class="event-date">MAY 11, 2019</p>

  <svg class="info-disc" viewBox="0 0 900 1200" aria-hidden="true">
    <circle cx="198" cy="1040" r="367" fill="none" stroke="var(--blue)" stroke-width="22"/>
    <circle cx="198" cy="1040" r="345" fill="none" stroke="var(--red)" stroke-width="24"/>
    <circle cx="198" cy="1040" r="319" fill="none" stroke="var(--yellow)" stroke-width="30"/>
    <circle cx="198" cy="1040" r="305" fill="var(--white)"/>
  </svg>

  <form class="club-form">
    <div class="form-row"><span class="label">NAME:</span><span class="line"></span></div>
    <div class="form-row"><span class="label">DATE:</span><span class="line"></span></div>
    <div class="form-row"><span class="label">LOCATION:</span><span class="line"></span></div>
    <div class="form-row"><span class="line"></span></div>
    <div class="form-row"><span class="label">TIME:</span><span class="line"></span></div>
    <div class="form-row"><span class="label">E-MAIL:</span><span class="line"></span></div>
    <div class="form-row"><span class="label">WEBSITE:</span><span class="line"></span></div>
    <div class="form-row"><span class="label">NOTES:</span><span class="line"></span></div>
    <div class="form-row"><span class="line"></span></div>
  </form>

  <div class="partners" aria-label="Partner badges">
    <span class="partner round"></span>
    <span class="partner round"></span>
    <span class="partner wide"></span>
    <span class="partner mid"></span>
    <span class="partner small"></span>
  </div>
</main>
</body>
</html>
```